Oil & Gas companies needs print design panels for Australia's biggest conference of 2016!

We need artwork design for 2 companies that are linked from Perth, Western Australia (KRV and Dulmora). Logos (in EPS format) have been attached.

Our websites (so that you can get a feel for what we do) are:
www.fenbrackworks.example
www.dulmora.example

We need two panels for our stand at the WIRLU conference in Brisbane. An image of the stand setup has been provided in the attached images. The panel artwork sizes required are:
1x 985mm x 2349mm h
1x 2349mm x 985mm h

A copy of the guidelines that need to be followed in order to have the artwork correctly displayed have also been attached.

WORDING FOR PANELS

KRV (logo) – panel
TAG LINE: KRV. Your Ally for Progress.
Completions and Commissioning,
Operational Readiness
Specialist Inspections,
Whatever your projects requirements,
Wherever you operate,
Whatever your schedule.
KRV keeps your venture moving forward.

Dulmora (logo) – panel
TAG LINE: Keep your assets under control.
Maintain plant safety.
Avoid unplanned downtime.
Comply with complex regulatory requirements.
Dulmora Hazardous Area and specialist inspection services.
Your Asset. Our Protection.

We need to x2 pics (from the ones supplied/or ones to do with Oil & Gas industry)

Target Market(s)

Conference
Oil & Gas professionals

Industry/Entity Type

Oil And Gas

Font styles to use
Sans Serif
Other font styles liked:
• DIN Offc

Requirements
Must have
• KRV & Dulmora Logo (one per panel)
• Must follow the attached guidelines provided from WIRLU.
• The KRV panel must be engaging and draw clients towards our stand as it is the first thing they will see when entering the conference.
• KRV & Dulmora colours:
• orange = #D76927, R-215 G-105 B-39, CMYK C-11.65 M-70.4 Y-100 K-1.52
• Blue = #21224B, R-33 G-34 B-75, CMYK C-95.65, M-92.65 Y-39.82, K40.01
Nice to have
• We would like to see some examples of faded pictures with wording more predominant.
• KRV:
• Completions and Commissioning - pop out/bold/stand out
• Operational Readiness - pop out/bold/stand out
• Inspections - pop out/bold/stand out
• Dulmora:
• Hazardous Area - pop out/bold/standout
Should not have
• Combined KRV/Dulmora panels - need to be separate

```html
<!DOCTYPE html>
<html lang="en">
<head>
<meta charset="utf-8">
<title>KRV – Your Ally for Progress</title>
<link rel="stylesheet" href="https://fonts.googleapis.com/css2?family=Barlow:wght@500;600;700;800&family=Barlow+Semi+Condensed:wght@700&display=swap">
<style>
  :root {
    --krv-orange: #D76927;
    --krv-navy: #21224B;
    --panel-grey: #DCDCDD;
    --night-deep: #14171c;
    --night-mid: #262a31;
    --plant-green: #3f5a4c;
    --plant-light: #8a9a86;
    --white: #ffffff;
  }
  * { margin: 0; padding: 0; box-sizing: border-box; }
  html, body {
    width: 1200px; height: 503px; overflow: hidden; background: var(--white);
  }
  .banner {
    position: relative; width: 1200px; height: 503px; overflow: hidden;
    font-family: "Barlow", Arial, sans-serif;
  }
  .plant-photo {
    position: absolute; left: 0; top: 0; width: 1200px; height: 448px;
    background:
      radial-gradient(ellipse 520px 150px at 760px 440px, rgba(138,154,134,0.55), rgba(138,154,134,0) 70%),
      radial-gradient(ellipse 420px 120px at 1090px 420px, rgba(138,154,134,0.4), rgba(138,154,134,0) 70%),
      linear-gradient(180deg, var(--night-deep) 0%, var(--night-mid) 55%, var(--plant-green) 100%);
  }
  .banner-shapes { position: absolute; left: 0; top: 0; }
  .brand {
    position: absolute; left: 50px; top: 50px;
    font-weight: 800; font-size: 112px; line-height: 1;
    letter-spacing: 4px; color: var(--krv-navy);
  }
  .services {
    position: absolute; left: 50px; top: 256px;
    list-style: none; color: var(--krv-navy);
    font-weight: 500; font-size: 16px; line-height: 21px;
  }
  .services .key-service { font-weight: 700; }
  .closing-line {
    position: absolute; left: 50px; top: 387px;
    font-family: "Barlow Semi Condensed", Arial, sans-serif;
    font-weight: 700; font-size: 17px; line-height: 21px; color: var(--krv-navy);
  }
  .headline {
    position: absolute; left: 668px; top: 46px;
    color: var(--white); font-weight: 700;
    font-size: 68px; line-height: 76px; letter-spacing: 2px;
    text-transform: uppercase;
  }
  .footer-band {
    position: absolute; left: 0; top: 446px; width: 1200px; height: 57px;
    background: var(--krv-orange); border-top: 2px solid var(--white);
    display: flex; align-items: center; justify-content: center;
  }
  .web-address {
    color: var(--white); font-weight: 700; font-size: 27px; letter-spacing: 0.5px;
  }
</style>
</head>
<body>
<div class="banner">
  <div class="plant-photo" role="img" aria-label="Photograph of an oil refinery at night with a red and white striped chimney, lit processing towers, a conveyor bridge and drifting steam"></div>

  <svg class="banner-shapes" width="1200" height="448" viewBox="0 0 1200 448" aria-hidden="true">
    <path class="accent-curve" d="M0 0 H426 C446 140 440 300 398 448 H0 Z" fill="var(--krv-orange)"/>
    <path class="text-panel" d="M0 0 H364 C420 90 436 240 394 448 H0 Z" fill="var(--panel-grey)"/>
  </svg>

  <div class="brand">KRV</div>

  <ul class="services">
    <li class="key-service">Completions and Commissioning,</li>
    <li class="key-service">Operational Readiness,</li>
    <li class="key-service">Specialist Inspections,</li>
    <li>Whatever your projects requirements,</li>
    <li>Wherever you operate,</li>
    <li>Whatever your schedule.</li>
  </ul>
  <p class="closing-line">KRV keeps your venture moving forward!</p>

  <h1 class="headline">Your Ally<br>for Progress</h1>

  <div class="footer-band">
    <span class="web-address">www.fenbrackworks.example</span>
  </div>
</div>
</body>
</html>
```